We need a flyer design to promote Penhallow & Tibbs Landscaping and Lawn Maintenance.

The flyer needs to be have:-
1) A great head line ( When quality matters)
2) A really awesome offer ( no obligation free trial mow)
3) A sense of scarcity (Due to time restraints, we can only take limited number of free lawn jobs. This offer is only available to the first 20 callers)
4) A call to action (Call now to avoid disappointment)
5) Contact details (Penhallow & Tibbs Landscaping and Lawn Maintenance 0452 786 305)

The layout of the entire flyer should come across to potential customers as

1) simple to understand what Penhallow & Tibbs offer (not overcrowd with messages; the main aim is to communicate across our services.)

The list of services that Penhallow & Tibbs provide will be:-

- Lawn Mowing - Pruning - Weeding
- Mulching - Edging - Hedging
- Trimming - Fertilising - Garden maintenance
- Weekly, fortnightly or monthly programs

Thank you.

```html
<!DOCTYPE html>
<html lang="en">
<head>
<meta charset="utf-8">
<title>Penhallow &amp; Tibbs Landscaping Flyer</title>
<link rel="stylesheet" href="https://fonts.googleapis.com/css2?family=Playfair+Display:wght@700;900&family=Cinzel:wght@600;700&family=Muli:wght@400&family=Oswald:wght@300;400&family=Vollkorn:wght@700&family=Roboto+Condensed:wght@400;700&display=swap">
<style>
  :root {
    --page: #ffffff;
    --frame-outer: #8fc77a;
    --frame-inner: #4f9a3c;
    --paper-edge: #b9dca4;
    --paper-mid: #e6f2dc;
    --paper-light: #fbfdf8;
    --brown-light: #b0622c;
    --brown-mid: #7a3e18;
    --brown-dark: #2a1408;
    --name-brown: #3e2d20;
    --leaf-green: #6aa84f;
    --navy: #0f2a5c;
    --offer-green: #2f5a16;
    --note: #f3e7a6;
    --note-edge: #d9c97a;
    --pin: #1f5fd0;
  }
  html, body {
    margin: 0;
    width: 1200px;
    height: 1028px;
    overflow: hidden;
    background: var(--page);
  }
  .canvas {
    position: relative;
    width: 1200px;
    height: 1028px;
  }
  .flyer {
    position: absolute;
    left: 270px;
    top: 0;
    width: 730px;
    height: 1028px;
    background: var(--frame-outer);
  }
  .flyer-inner {
    position: absolute;
    left: 10px; top: 8px; right: 8px; bottom: 8px;
    border: 4px solid var(--frame-inner);
    background: radial-gradient(ellipse 60% 55% at 52% 45%, var(--paper-light) 0%, var(--paper-mid) 60%, var(--paper-edge) 100%);
    box-shadow: inset 0 0 0 8px rgba(255,255,255,0.35);
    overflow: hidden;
  }
  .headline {
    position: absolute;
    left: 0; right: 0; top: 22px;
    margin: 0;
    text-align: center;
    font-family: "Playfair Display", serif;
    font-weight: 900;
    font-size: 112px;
    line-height: 110px;
    letter-spacing: -2px;
  }
  .headline-line {
    display: block;
    transform: scaleX(0.78);
    -webkit-background-clip: text;
    background-clip: text;
    -webkit-text-fill-color: transparent;
    color: transparent;
  }
  .headline-line.first { background-image: linear-gradient(180deg, var(--brown-light) 20%, var(--brown-mid) 100%); }
  .headline-line.second { background-image: linear-gradient(180deg, var(--brown-mid) 10%, var(--brown-dark) 80%); }
  .company {
    position: absolute;
    left: 0; right: 0; top: 250px;
    text-align: center;
    font-family: "Cinzel", serif;
    font-weight: 700;
    font-size: 64px;
    line-height: 66px;
    color: var(--name-brown);
    white-space: nowrap;
  }
  .trade {
    position: absolute;
    left: 20px; right: 0; top: 322px;
    text-align: center;
    font-family: "Muli", sans-serif;
    font-size: 32px;
    letter-spacing: 40px;
    color: var(--leaf-green);
    white-space: nowrap;
  }
  .trade-sub {
    position: absolute;
    left: 0; right: 0; top: 368px;
    text-align: center;
    font-family: "Cinzel", serif;
    font-weight: 600;
    font-size: 36px;
    color: var(--name-brown);
    white-space: nowrap;
  }
  .photo {
    position: absolute;
    left: 20px; top: 420px;
    width: 650px; height: 420px;
    background: radial-gradient(ellipse 55% 50% at 50% 55%, #7e8f70 0%, #5f8f3e 45%, rgba(120,180,80,0.6) 70%, rgba(230,242,220,0) 100%);
  }
  .note {
    position: absolute;
    left: 218px; top: 500px;
    width: 245px; height: 150px;
    background: var(--note);
    border: 1px solid var(--note-edge);
    box-shadow: 2px 4px 8px rgba(0,0,0,0.3);
    transform: rotate(-6deg);
    transform-origin: top left;
    font-family: "Roboto Condensed", sans-serif;
    text-align: center;
  }
  .note-pin {
    position: absolute;
    left: 104px; top: 10px;
  }
  .note-title {
    margin: 42px 0 0;
    font-size: 44px;
    font-weight: 700;
    color: var(--navy);
    line-height: 44px;
  }
  .note-text {
    margin: 2px 0 0;
    font-size: 25px;
    color: var(--offer-green);
    line-height: 24px;
  }
  .offer {
    position: absolute;
    left: 0; right: 0; top: 744px;
    text-align: center;
    font-family: "Roboto Condensed", sans-serif;
    font-size: 35px;
    color: var(--navy);
  }
  .phone {
    position: absolute;
    left: 0; right: 0; top: 768px;
    text-align: center;
    font-family: "Oswald", sans-serif;
    font-weight: 300;
    font-size: 98px;
    line-height: 120px;
    color: var(--navy);
  }
  .rule {
    position: absolute;
    left: 38px; right: 38px; top: 885px;
    height: 3px;
    background: var(--offer-green);
  }
  .scarcity {
    position: absolute;
    left: 20px; right: 20px; top: 896px;
    margin: 0;
    text-align: center;
    font-family: "Vollkorn", serif;
    font-weight: 700;
    font-size: 25px;
    line-height: 32px;
    color: var(--offer-green);
  }
</style>
</head>
<body>
<div class="canvas">
  <section class="flyer">
    <div class="flyer-inner">
      <div class="photo" role="img" aria-label="Photo of a grey two-storey house with a neatly mown green lawn, flower beds and trees"></div>

      <h1 class="headline"><span class="headline-line first">When quality</span><span class="headline-line second">matters</span></h1>
      <div class="company">Penhallow &amp; Tibbs</div>
      <div class="trade">LANDSCAPING</div>
      <div class="trade-sub">and Lawn Maintenance</div>

      <div class="note">
        <svg class="note-pin" width="36" height="36" viewBox="0 0 36 36" aria-hidden="true">
          <circle cx="18" cy="18" r="15" fill="var(--pin)"/>
        </svg>
        <p class="note-title">CALL NOW</p>
        <p class="note-text">to avoid<br>disappointment</p>
      </div>

      <div class="offer">No Obligation Free Trial</div>
      <div class="phone">0452 786 305</div>
      <div class="rule"></div>
      <p class="scarcity">Due to time restraints, we can only take limited<br>number of free lawn jobs.<br>This offer is only available to the first 20 callers</p>
    </div>
  </section>
</div>
</body>
</html>
```